business cards for heating company

I need business cards for my heating air conditioning and chimney company located in upstate NY I would like for them to be colorful and catchy on heavy stock with preferably a glossy finish on front of card but the ability to write something on one half of the back with maybe some bullets on the other half of the back I also need to be able to change the name and title of employees on the card and also incorporate some of our current look and feel from our trucks and website I also want to be able to use this design or similar to have door hangers made lawn signs coffee mugs key chains etc. our website is Brindlecove.com

Target Market(s)

homeowners

Industry/Entity Type

Air Conditioning

Contact Information for Business Card

should have website brindlecove.com , phone number 585-437-9184 please look at website for ideas

Font styles to use
Sans Serif

Colors
ec1f27
3176b5
fbee3f

Requirements
Must have
• a complete look
Nice to have
• a discount offer like 10% military and first responders
• senior discount %5

```html
<!DOCTYPE html>
<html lang="en">
<head>
<meta charset="utf-8">
<title>Brindlecove Business Card</title>
<link href="https://fonts.googleapis.com/css2?family=Exo+2:wght@400;600;800&display=swap" rel="stylesheet">
<style>
  :root {
    --page-bg: #e6e6e8;
    --card-white: #ffffff;
    --card-shade: #e9e9ea;
    --brand-magenta: #c8175f;
    --brand-blue: #0a56ee;
    --ink: #2b2b2b;
    --ink-soft: #3c3c3c;
  }
  * { margin: 0; padding: 0; box-sizing: border-box; }
  html, body {
    width: 1200px; height: 900px; overflow: hidden;
    background: var(--page-bg);
    font-family: "Exo 2", sans-serif;
  }
  .canvas { position: relative; width: 1200px; height: 900px; }
  .business-card {
    position: absolute; left: 110px; top: 170px;
    width: 980px; height: 560px;
    border-radius: 44px; overflow: hidden;
    background: radial-gradient(ellipse at 45% 40%, var(--card-white) 0%, var(--card-white) 35%, var(--card-shade) 100%);
    box-shadow: 0 18px 40px rgba(0,0,0,0.18);
  }
  .wave-bands { position: absolute; inset: 0; width: 100%; height: 100%; }
  .brand-block { position: absolute; left: 48px; top: 140px; }
  .brand-name {
    font-weight: 800; font-size: 58px; letter-spacing: 1px;
    color: var(--brand-magenta); line-height: 1;
  }
  .brand-tagline {
    margin-top: 8px;
    font-weight: 600; font-size: 27px; letter-spacing: 0.5px;
    color: var(--brand-blue);
  }
  .contact-block {
    position: absolute; right: 70px; top: 36px;
    text-align: right; color: var(--ink);
  }
  .person-name { font-weight: 600; font-size: 30px; letter-spacing: 2px; line-height: 1.2; }
  .person-title { font-size: 20px; color: var(--ink-soft); margin-top: 2px; }
  .address { font-size: 20px; line-height: 1.3; margin-top: 24px; color: var(--ink-soft); }
  .contact-list { list-style: none; margin-top: 18px; }
  .contact-list li {
    display: flex; justify-content: flex-end; align-items: center;
    gap: 10px; font-size: 16px; line-height: 1.5; color: var(--ink-soft);
  }
  .contact-icon { width: 15px; height: 15px; fill: var(--ink); }
</style>
</head>
<body>
<main class="canvas">
  <section class="business-card">
    <svg class="wave-bands" viewBox="0 0 980 560" preserveAspectRatio="none" aria-hidden="true">
      <path fill="var(--brand-blue)" d="M0,430 C200,395 420,420 600,405 C780,390 900,380 980,345 L980,560 L0,560 Z"/>
      <path fill="#ffffff" d="M0,492 C200,462 420,462 600,440 C780,420 900,405 980,372 L980,560 L0,560 Z"/>
      <path fill="var(--brand-magenta)" d="M0,508 C200,478 420,478 600,456 C780,436 900,420 980,388 L980,560 L0,560 Z"/>
    </svg>

    <div class="brand-block">
      <div class="brand-name">BRINDLECOVE</div>
      <div class="brand-tagline">HEATING, COOLING &amp; CHIMNEY</div>
    </div>

    <div class="contact-block">
      <div class="person-name">DANIEL WHITCOMB</div>
      <div class="person-title">Managing Director</div>
      <div class="address">214 Orchard Lane,<br>Fairport NY</div>
      <ul class="contact-list">
        <li>585-437-9184
          <svg class="contact-icon" viewBox="0 0 24 24"><path d="M6.6 10.8a15 15 0 0 0 6.6 6.6l2.2-2.2a1 1 0 0 1 1-.25 11.4 11.4 0 0 0 3.6.57 1 1 0 0 1 1 1V20a1 1 0 0 1-1 1A17 17 0 0 1 3 4a1 1 0 0 1 1-1h3.5a1 1 0 0 1 1 1c0 1.25.2 2.450.57 3.6a1 1 0 0 1-.25 1z"/></svg>
        </li>
        <li>585-437-9184
          <svg class="contact-icon" viewBox="0 0 24 24"><path d="M7 1h10a2 2 0 0 1 2 2v18a2 2 0 0 1-2 2H7a2 2 0 0 1-2-2V3a2 2 0 0 1 2-2zm0 3v14h10V4zm5 15.5a1 1 0 1 0 0 2 1 1 0 0 0 0-2z"/></svg>
        </li>
        <li>585-437-9184
          <svg class="contact-icon" viewBox="0 0 24 24"><path d="M6 2h10v5H6zM3 8h18a1 1 0 0 1 1 1v8h-4v5H6v-5H2V9a1 1 0 0 1 1-1zm5 7v5h8v-5z"/></svg>
        </li>
        <li>info@brindlecove.com
          <svg class="contact-icon" viewBox="0 0 24 24"><path d="M2 5h20v14H2zm2 2v.5l8 5 8-5V7zm0 2.9V17h16V9.9l-8 5z"/></svg>
        </li>
        <li>www.brindlecove.com
          <svg class="contact-icon" viewBox="0 0 24 24"><path d="M12 2a10 10 0 1 0 0 20 10 10 0 0 0 0-20zm6.9 9h-3a15 15 0 0 0-1.3-5.6A8 8 0 0 1 18.9 11zM12 4.1c.9 1.2 1.7 3.6 1.9 6.9h-3.8c.2-3.3 1-5.7 1.9-6.9zM9.4 5.4A15 15 0 0 0 8.1 11h-3a8 8 0 0 1 4.3-5.6zM5.1 13h3a15 15 0 0 0 1.3 5.6A8 8 0 0 1 5.1 13zm6.9 6.9c-.9-1.2-1.7-3.6-1.9-6.9h3.8c-.2 3.3-1 5.7-1.9 6.9zm2.6-1.3a15 15 0 0 0 1.3-5.6h3a8 8 0 0 1-4.3 5.6z"/></svg>
        </li>
      </ul>
    </div>
  </section>
</main>
</body>
</html>
```